Business Card for Maplethorne Elder Keepers

I need a business card design for a very elite and personalized companion care company. We take care of the client at home with respect, dignity, and our full attention. The design should communicate a classic elegance and trust.

/Users/lorafenwick/Downloads/graphwellhub_121488_23943024_3826329_sourcefile

```html
<!DOCTYPE html>
<html lang="en">
<head>
<meta charset="utf-8">
<title>Maplethorne Elder Keepers — Business Card</title>
<link rel="stylesheet" href="https://fonts.googleapis.com/css2?family=Cinzel:wght@500&family=Cormorant+Garamond:ital,wght@1,500&family=Crimson+Text&display=swap">
<style>
  :root {
    --navy: #0b4a86;
    --sky: #12aee6;
    --ink-gray: #6f6f6f;
    --paper: #f6f6f4;
    --backdrop: #e4e4e4;
  }
  html, body {
    margin: 0;
    width: 1200px;
    height: 900px;
    overflow: hidden;
    background: var(--backdrop);
  }
  .card {
    position: absolute;
    left: 75px;
    top: 150px;
    width: 1050px;
    height: 600px;
    background: var(--paper);
    overflow: hidden;
    box-shadow: 0 6px 22px rgba(0,0,0,0.12);
  }
  .brand {
    position: absolute;
    left: 62px;
    top: 66px;
    display: flex;
    align-items: flex-start;
    gap: 14px;
  }
  .brand-dot {
    width: 22px;
    height: 22px;
    border-radius: 50%;
    background: var(--sky);
    margin-top: 6px;
  }
  .brand-name {
    margin: 0;
    font-family: "Cinzel", serif;
    font-weight: 500;
    font-size: 42px;
    line-height: 1.1;
    color: var(--navy);
    letter-spacing: 0.5px;
  }
  .person {
    position: absolute;
    right: 62px;
    top: 272px;
    text-align: right;
  }
  .person-name {
    margin: 0;
    font-family: "Cinzel", serif;
    font-weight: 500;
    font-size: 38px;
    color: var(--navy);
    letter-spacing: 0.5px;
  }
  .person-role {
    margin: 0;
    font-family: "Cormorant Garamond", serif;
    font-style: italic;
    font-weight: 500;
    font-size: 30px;
    color: var(--sky);
    line-height: 1;
  }
  .contact, .address {
    position: absolute;
    top: 418px;
    margin: 0;
    font-family: "Crimson Text", serif;
    font-size: 27px;
    line-height: 37px;
    color: var(--ink-gray);
    font-style: normal;
  }
  .contact { left: 62px; }
  .address { right: 58px; text-align: right; }
  .wave {
    position: absolute;
    left: 0;
    bottom: 0;
    width: 1050px;
    height: 120px;
  }
</style>
</head>
<body>
  <section class="card">
    <div class="brand">
      <h1 class="brand-name">Maplethorne<br>Elder Keepers</h1>
      <span class="brand-dot"></span>
    </div>

    <div class="person">
      <p class="person-name">Lora Fenwick</p>
      <p class="person-role">Founder</p>
    </div>

    <p class="contact">555-014-2288<br>name@mail.com</p>
    <address class="address">418 NW Harrow Lane, Cedar Vale,<br>FL 34000, USA</address>

    <svg class="wave" viewBox="0 0 1050 120" preserveAspectRatio="none" aria-hidden="true">
      <path d="M0,116 C350,72 800,96 1050,0 L1050,120 L0,120 Z" fill="var(--sky)"/>
      <path d="M0,120 C380,86 820,102 1050,24 L1050,120 Z" fill="var(--navy)"/>
    </svg>
  </section>
</body>
</html>
```